Pedalwise Touring Co Brochure

We need an informational brochure designed to display all of our cycling tours for the 2019 season. The majority of text and images can be pulled from our website - www.pedalwisetouringco.example

We would like to use the colors red (#242424), Grey, and White

```html
<!DOCTYPE html>
<html lang="en">
<head>
<meta charset="utf-8">
<title>Pedalwise Touring Co – Utah's Slickrock and Singletrack</title>
<link href="https://fonts.googleapis.com/css2?family=Oswald:wght@400;500;600&family=Roboto+Condensed:ital,wght@0,300;0,400;0,700;1,300&display=swap" rel="stylesheet">
<style>
  :root {
    --red: #b52634;
    --grey: #7b7b7b;
    --grey-light: #8d8d8d;
    --white: #ffffff;
    --ink: #1d1d1d;
  }
  * { box-sizing: border-box; margin: 0; padding: 0; }
  html, body { width: 848px; height: 1200px; overflow: hidden; background: var(--white); }
  .brochure {
    position: relative; width: 848px; height: 1200px; overflow: hidden;
    background: var(--white); color: var(--ink);
    font-family: "Roboto Condensed", sans-serif;
  }
  .abs { position: absolute; }

  /* Header */
  .brand { left: 0; top: 0; width: 307px; height: 108px; display: flex; align-items: center; gap: 12px; padding-left: 30px; }
  .brand-dot { width: 72px; height: 72px; border-radius: 50%; border: 4px solid var(--red); flex: none; }
  .brand-name { font-family: "Oswald", sans-serif; font-weight: 500; font-size: 25px; line-height: 1.05; color: var(--red); }
  .title-band { left: 307px; top: 0; width: 541px; height: 108px; background: var(--red); display: flex; align-items: center; justify-content: center; }
  .title-band h1 { font-family: "Oswald", sans-serif; font-weight: 600; font-size: 37px; color: var(--white); letter-spacing: 0.2px; }

  /* Photo areas */
  .photo { display: block; }
  .hero { left: 0; top: 108px; width: 848px; height: 297px;
    background: linear-gradient(180deg, #aebfd3 0%, #c9d3dc 22%, #7f7865 36%, #a86b4d 52%, #50603a 70%, #3c5030 100%); }
  .price { left: 741px; top: 126px; width: 84px; height: 84px; border-radius: 50%; background: var(--grey);
    color: var(--white); font-family: "Oswald", sans-serif; font-weight: 500; font-size: 19px; line-height: 1.25;
    display: flex; flex-direction: column; align-items: center; justify-content: center; }

  /* Departures */
  .departures { left: 0; top: 405px; width: 162px; height: 451px; background: var(--red); }
  .departures h2 { position: absolute; left: 20px; top: 6px; font-family: "Oswald", sans-serif; font-weight: 600;
    font-size: 24px; line-height: 30px; color: var(--white); letter-spacing: 0.3px; }
  .date-list { position: absolute; left: 20px; top: 69px; width: 123px; height: 362px; background: var(--white);
    list-style: none; padding: 4px 4px; font-size: 15.5px; line-height: 20.5px; font-weight: 300; }
  .date-list li { text-align: left; }
  .date-list .bike { display: block; margin: 1px auto 0; width: 18px; height: 11px; }

  .grey-left { left: 0; top: 856px; width: 162px; height: 344px; background: var(--grey); }
  .photo-arch { left: 8px; top: 864px; width: 146px; height: 326px;
    background: linear-gradient(160deg, #d98a3a 0%, #b8612b 35%, #8fa8c4 60%, #5e5a4c 100%); }

  .grey-right { left: 478px; top: 606px; width: 370px; height: 594px; background: var(--grey); }
  .grey-strip { left: 676px; top: 405px; width: 172px; height: 201px; background: var(--grey); }
  .photo-trail { left: 685px; top: 413px; width: 154px; height: 477px;
    background: linear-gradient(180deg, #4a87c4 0%, #c8642d 24%, #8a6a4a 45%, #7d7468 100%); }
  .photo-jump { left: 486px; top: 624px; width: 189px; height: 266px;
    background: linear-gradient(180deg, #5f7a45 0%, #3f5a31 50%, #6c5a3e 100%); }
  .photo-peak { left: 486px; top: 899px; width: 353px; height: 141px;
    background: linear-gradient(180deg, #dfe3e5 0%, #c27a4f 40%, #5f7a3e 75%, #3f5e2a 100%); }
  .photo-canyon { left: 486px; top: 1051px; width: 353px; height: 139px;
    background: linear-gradient(180deg, #a9bccc 0%, #8a6c5b 30%, #b45a3a 60%, #c88a5e 100%); }

  /* Facts */
  .facts { display: grid; grid-template-columns: auto auto; column-gap: 18px; row-gap: 1px; font-size: 16px; line-height: 20px; }
  .facts dt { font-style: italic; font-weight: 300; }
  .facts dd { font-weight: 400; }
  .facts-trip { left: 186px; top: 414px; column-gap: 44px; }
  .facts-travel { left: 440px; top: 414px; column-gap: 14px; }

  /* Body copy */
  .copy { left: 168px; top: 491px; width: 508px; }
  .spacer-top { float: right; width: 0; height: 130px; }
  .spacer-photo { float: right; clear: right; width: 198px; height: 290px; }
  .copy h3 { font-family: "Roboto Condensed", sans-serif; font-weight: 700; font-size: 19px; line-height: 24px; }
  .summary { font-size: 14.3px; line-height: 18.8px; font-weight: 300; margin-right: 0; }
  .copy h4 { font-weight: 700; font-size: 15px; line-height: 19px; margin: 6px 0 0 4px; }
  .bullets { list-style: none; font-size: 13.2px; line-height: 18px; font-weight: 300; margin-left: 17px; }
  .bullets li { padding-left: 11px; text-indent: -11px; }
  .bullets li::before { content: ""; display: inline-block; width: 8px; height: 8px; border-radius: 50%;
    background: #5a5a5a; margin-right: 3px; vertical-align: 0; }
</style>
</head>
<body>
<main class="brochure">

  <header>
    <div class="abs brand">
      <span class="brand-dot"></span>
      <span class="brand-name">Pedalwise<br>Touring Co</span>
    </div>
    <div class="abs title-band"><h1>Utah’s Slickrock and Singletrack</h1></div>
  </header>

  <div class="abs photo hero" role="img" aria-label="Two mountain bikers on a rocky overlook above forested red-rock canyon country"></div>
  <div class="abs price"><span>Price:</span><span>US $2395</span></div>

  <section class="abs departures">
    <h2>DEPARTURE<br>DATES</h2>
    <ul class="date-list">
      <li>June 9th, 2019 –<br>June 14th, 2019
        <svg class="bike" viewBox="0 0 18 11" fill="none" stroke="#333" stroke-width="1"><circle cx="4" cy="7" r="3.3"/><circle cx="14" cy="7" r="3.3"/><path d="M4 7 L7 2.5 H12 L14 7 M7 2.5 L9 7 L12 2.5 M6 1.5 H8"/></svg></li>
      <li>June 16th, 2019 –<br>June 21th, 2019
        <svg class="bike" viewBox="0 0 18 11" fill="none" stroke="#333" stroke-width="1"><circle cx="4" cy="7" r="3.3"/><circle cx="14" cy="7" r="3.3"/><path d="M4 7 L7 2.5 H12 L14 7 M7 2.5 L9 7 L12 2.5 M6 1.5 H8"/></svg></li>
      <li>July 21st, 2019 –<br>July 26th, 2019
        <svg class="bike" viewBox="0 0 18 11" fill="none" stroke="#333" stroke-width="1"><circle cx="4" cy="7" r="3.3"/><circle cx="14" cy="7" r="3.3"/><path d="M4 7 L7 2.5 H12 L14 7 M7 2.5 L9 7 L12 2.5 M6 1.5 H8"/></svg></li>
      <li>July 28th, 2019 –<br>Aug 2nd, 2019
        <svg class="bike" viewBox="0 0 18 11" fill="none" stroke="#333" stroke-width="1"><circle cx="4" cy="7" r="3.3"/><circle cx="14" cy="7" r="3.3"/><path d="M4 7 L7 2.5 H12 L14 7 M7 2.5 L9 7 L12 2.5 M6 1.5 H8"/></svg></li>
      <li>Sept 1st, 2019 –<br>Sept 6th, 2019
        <svg class="bike" viewBox="0 0 18 11" fill="none" stroke="#333" stroke-width="1"><circle cx="4" cy="7" r="3.3"/><circle cx="14" cy="7" r="3.3"/><path d="M4 7 L7 2.5 H12 L14 7 M7 2.5 L9 7 L12 2.5 M6 1.5 H8"/></svg></li>
      <li>Sept 8th, 2019 –<br>Sept 13th, 2019</li>
    </ul>
  </section>

  <div class="abs grey-left"></div>
  <div class="abs photo photo-arch" role="img" aria-label="Rider descending beneath an orange sandstone arch"></div>

  <div class="abs grey-strip"></div>
  <div class="abs grey-right"></div>
  <div class="abs photo photo-trail" role="img" aria-label="Rider in blue on a rocky trail below glowing red canyon walls"></div>
  <div class="abs photo photo-jump" role="img" aria-label="Rider jumping off a wooden feature in a pine forest"></div>
  <div class="abs photo photo-peak" role="img" aria-label="Sunlit red peak rising above green river valley"></div>
  <div class="abs photo photo-canyon" role="img" aria-label="Singletrack ridge above eroded red-rock amphitheatre"></div>

  <dl class="abs facts facts-trip">
    <dt>Duration:</dt><dd>6 Days / 5 Nights</dd>
    <dt>Availability:</dt><dd>Summer 2019</dd>
    <dt>Group Size:</dt><dd>Max 12</dd>
  </dl>
  <dl class="abs facts facts-travel">
    <dt>Departure City:</dt><dd>Las Vegas, NV</dd>
    <dt>Ends In:</dt><dd>Las Vegas, NV</dd>
    <dt>Accommodation:</dt><dd>3-4 Star Hotels</dd>
  </dl>

  <article class="abs copy">
    <div class="spacer-top"></div>
    <div class="spacer-photo"></div>
    <h3>Trip Summary</h3>
    <p class="summary">Southern Utah’s canyon country is renowned for its incredible multi colored cliffs, valleys, red rock monoliths, and singletrack trails. Shaped by billions of years of erosion, this alien landscape emerged as a true adventurer’s playground. Hundreds of miles of singletrack trails wind over smooth outcroppings of weathered sandstone, known as slickrock. The ideal riding surface for mountain biking, slickrock provides a high level of grip, and stability, allowing riders to conquer even the gnarliest of obstacles. Expect a smorgasbord of turns, quick drops, short climbs, and no shortage of technical features that will push your balance, and ability as a rider. Spectacular vistas lie around every corner, and the unique beauty and colors of Utah will leave you in awe.</p>
    <h4>Inclusions</h4>
    <ul class="bullets">
      <li>Cycling Expert and ‘on the road’ support staff and vehicle</li>
      <li>Custom Fitting on 2018 Ridgeline Trailhawk Carbon 27.5</li>
      <li>5 nights’ accommodation as per the itinerary</li>
      <li>Supported Rest/Lunch stops</li>
      <li>Luggage Transfer each day</li>
      <li>Snacks/Drinks for the ride</li>
      <li>Dinner in Canyon Tap House</li>
      <li>Lunch in Hurricane</li>
      <li>Dinner in Brianhead</li>
      <li>Zion National Park</li>
      <li>Bryce Canyon National Park</li>
      <li>Massage and Spa Entrance</li>
      <li>Use of Waypoint GPS Unit</li>
      <li>Canyon Tap House Send Off</li>
    </ul>
    <h4 style="margin-top:2px">Featured Rides</h4>
    <ul class="bullets">
      <li>Gooseberry Mesa</li>
      <li>Hurricane Rim Trail</li>
      <li>Thunder Mountain Trail</li>
      <li>Virgin River Rim Trail</li>
      <li>Brianhead Mountain Bike Park</li>
    </ul>
  </article>

</main>
</body>
</html>
```